UP:LOOM HERE Flyer

UP:LOOM HERE is a social enterprise that aims to promote sustainability through enabling and interacting with the community at large by prolonging the life of our preloved apparels that promote green habits such as reusing, repurposing and recreating.

The task is to create a double sided A5 flyer that targets Crafters, Sewists and Hobbyists to book and rent our Creative Spaces for their craft projects. We would also like to showcase our webstore for preloved clothing and upcycled merchandise. The design should be engaging to attract the young crowd.
Please visit our website www.uploomhere.sg and instagram (https://www.instagram.com/uploomheresg/) for reference on what we do.

Target Market(s)

Crafters, Sewists and Hobbyists. Young crowd between 16 to 45 years old

Requirements
Must have
• fun culture to create and upcycle fabric and to our part for the society
Heavy emphasis on Creative Spaces
Nice to have
• promote UP:LOOM HERE as the curated platform to source, supply and
contribute towards Circular Fashion.
Should not have
• Do not reflect us as a thrift store

```html
<!DOCTYPE html>
<html lang="en">
<head>
<meta charset="utf-8">
<title>Uploom Here Flyer</title>
<link href="https://fonts.googleapis.com/css2?family=Montserrat:wght@300;400;500;600;700;800&display=swap" rel="stylesheet">
<style>
  :root {
    --leaf: #5ea315;
    --forest: #1c7a18;
    --text-green: #4b9a1c;
    --orange-light: #fdc56b;
    --orange-deep: #f59e2c;
    --coral: #e8501c;
    --paper: #ffffff;
    --stage: #ffffff;
    --stage-low-top: #f2f2f2;
    --stage-low-bottom: #dcdcdc;
    --photo-dark: #3a2a1e;
    --photo-warm: #8a5a34;
  }
  * { margin: 0; padding: 0; box-sizing: border-box; }
  html, body { width: 1200px; height: 2502px; overflow: hidden; }
  body {
    position: relative;
    background: var(--stage);
    font-family: "Montserrat", sans-serif;
    color: var(--text-green);
  }
  .stage-floor {
    position: absolute; left: 0; top: 1491px; width: 1200px; height: 1011px;
    background: linear-gradient(180deg, var(--stage-low-top), var(--stage-low-bottom));
  }
  .page {
    position: absolute; background: var(--paper);
    box-shadow: 0 4px 18px rgba(0,0,0,0.08);
    overflow: hidden;
  }

  /* ---------- Front ---------- */
  .front { left: 193px; top: 151px; width: 497px; height: 697px; }
  .brand {
    position: absolute; left: 44px; top: 50px;
    display: flex; align-items: center; gap: 8px;
    font-weight: 700; font-size: 16px; color: var(--leaf); letter-spacing: 0.5px;
  }
  .brand-dot { width: 16px; height: 16px; border-radius: 50%; background: var(--leaf); }
  .front-photo {
    position: absolute; left: 0; top: 89px; width: 376px; height: 566px;
    background:
      radial-gradient(ellipse at 55% 75%, rgba(196,130,72,0.9), transparent 60%),
      linear-gradient(160deg, var(--photo-warm) 0%, var(--photo-dark) 45%, #5b3a22 100%);
  }
  .front-photo::after {
    content: ""; position: absolute; inset: 0;
    background: linear-gradient(180deg, rgba(0,0,0,0.1) 0%, rgba(0,0,0,0) 40%, rgba(40,25,15,0.55) 100%);
  }
  .front-url {
    position: absolute; left: 34px; top: 131px; z-index: 2;
    color: #fff; font-weight: 700; font-size: 11.5px;
  }
  .headline {
    position: absolute; left: 34px; top: 484px; z-index: 2;
    color: #fff; font-weight: 800; font-size: 35px; line-height: 43px;
  }
  .headline .mark { position: relative; display: inline-block; z-index: 0; }
  .headline .mark::before {
    content: ""; position: absolute; left: 0; right: 0; bottom: -3px; height: 16px;
    background: var(--leaf); z-index: -1;
  }
  .tagline {
    position: absolute; left: 34px; top: 595px; z-index: 2;
    color: #fff; font-weight: 300; font-size: 15px; line-height: 17px; width: 240px;
  }
  .block-leaf { position: absolute; left: 376px; top: 89px; width: 78px; height: 89px; background: var(--leaf); z-index: 2; }
  .block-forest { position: absolute; left: 376px; top: 143px; width: 121px; height: 512px; background: var(--forest); }
  .categories {
    position: absolute; left: 437px; top: 241px;
    writing-mode: vertical-rl; transform: translateX(-50%) rotate(180deg);
    color: #fff; font-size: 12px; font-weight: 500; white-space: nowrap;
  }
  .front-bar { position: absolute; left: 0; top: 685px; width: 497px; height: 12px; background: var(--leaf); }

  /* ---------- Back ---------- */
  .back { left: 518px; top: 921px; width: 488px; height: 684px; }
  .back-photo {
    position: absolute; left: 0; top: 32px; width: 488px; height: 269px;
    background: linear-gradient(100deg, var(--orange-light) 0%, #fab24a 55%, var(--orange-deep) 100%);
  }
  .back-block { position: absolute; left: 0; top: 13px; width: 200px; height: 36px; background: var(--leaf); }
  .visit { position: absolute; left: 40px; top: 193px; font-size: 11px; font-weight: 500; color: var(--coral); }
  .back-url { position: absolute; left: 40px; top: 210px; font-size: 13px; font-weight: 800; color: #fff; }

  .details { position: absolute; left: 40px; top: 348px; width: 262px; font-size: 6.8px; line-height: 8.3px; }
  .details .lead { font-weight: 600; }
  .details h3 { font-size: 7px; font-weight: 700; margin: 0 0 8px; }
  .details .section { margin-top: 16px; }
  .details .note { font-weight: 700; margin-top: 24px; }

  .location { position: absolute; left: 358px; top: 348px; width: 100px; font-size: 6.8px; line-height: 8.3px; }
  .location .strong { font-weight: 700; }
  .location p + p { margin-top: 9px; }

  .socials { position: absolute; left: 358px; top: 586px; font-size: 9px; font-weight: 500; }
  .social { display: flex; align-items: center; gap: 10px; height: 25px; }
  .social-dot { width: 13px; height: 13px; border-radius: 50%; border: 1.5px solid var(--leaf); }
  .back-bar { position: absolute; left: 0; top: 677px; width: 488px; height: 7px; background: var(--leaf); }
</style>
</head>
<body>
  <div class="stage-floor"></div>

  <section class="page front">
    <div class="brand"><span class="brand-dot"></span>UPLOOM HERE</div>
    <div class="front-photo" role="img" aria-label="Photo of a craftsman in a leather apron cutting leather pattern pieces at a workbench"></div>
    <div class="front-url">www.uploomhere.sg</div>
    <h1 class="headline">Sell Your Craft<br><span class="mark">and Creativity</span></h1>
    <p class="tagline">in the biggest creative people community</p>
    <div class="block-forest"></div>
    <div class="block-leaf"></div>
    <div class="categories">Men | Women | Children | Apparel | Craft | Merchandise | etc</div>
    <div class="front-bar"></div>
  </section>

  <section class="page back">
    <div class="back-photo" role="img" aria-label="Photo of a young woman in a straw hat and orange ruffled skirt dancing against an orange backdrop"></div>
    <div class="back-block"></div>
    <div class="visit">visit us mow</div>
    <div class="back-url">www.uploomhere.sg</div>

    <div class="details">
      <p class="lead">At Uploom Here Creative Spaces we offer MakerSpace or facilities for crafting, sewing and photo studio facilities.</p>
      <div class="section">
        <h3>Craft Space</h3>
        <p>For craft space or makerspace, we provide a tablespace for you to create crafts through hand embroidery, crocheting, weaving, beading, leatherworks and various fabric crafts. We provide tools and basic needs like glue, scissors, ruler and drawing materials.</p>
      </div>
      <div class="section" style="margin-top:28px">
        <h3>Sewing Space</h3>
        <p>For sewing space or makerspace, we provide a dedicated STITCHWELL sewing machine facility including the use of our cutting table and ironing space. Free use of special purpose footers and needles for leather, jersey and simple embroidery. Custom embroidery at additional charges based on design complexity and thread count.</p>
      </div>
      <p class="note">** Free use of pre-loved yarn and destashed fabric when you rent a Craft or Sewing Space at Creative Spaces.</p>
      <div class="section" style="margin-top:24px">
        <h3>Studio Space</h3>
        <p>For Studio Space, we provide functional studio facilities on our loft equipped with a mannequin, studio lighting and accessories. We also provide an enclosed studio box for photoshoot of small items like crafts, bottles etc. Camera available on site for loan.</p>
      </div>
    </div>

    <div class="location">
      <p class="strong">Our Creative Spaces shop office is located at</p>
      <p class="strong">22 Maple Crescent, Unit #03-18, S(512907)</p>
      <p>This is a commercial business space and located within 2 minutes walking distance from Maple bus terminal and MRT.</p>
    </div>

    <div class="socials">
      <div class="social"><span class="social-dot"></span>sguploomhere</div>
      <div class="social"><span class="social-dot"></span>uploomheresg</div>
    </div>
    <div class="back-bar"></div>
  </section>
</body>
</html>
```